Need Amazing Website for Consulting Company

We need an amazing website design for a Human Resources Consulting Company. This will be geared towards a more professional crowd, but we don't want it to be overly corporate and stuffy: Just, clean and professional and amazing. Please use the video link below for further instruction.

http://clipvarn.example/t/kzQmPoLe7

Thank You.

PS Logo file has been attached.

Target Market(s)

The target marketing is small business owners who have employees. These owners cant afford an in-house HR person so they would hire this client to consult and do the work for them.

Industry/Entity Type

It Company

Font styles to use
Sans Serif

Requirements
Must have
• Please watch video:

Must have spot for video on homepage.
Nice to have
• Clean, professional, but not overly corporate, we want a personal and fun feel to this site a bit to separate them from all the other executive type sites. This site should have some LIFE to it and reflect a local brand that is doing great things.
Should not have
• Should not be just a corporate site, should not be overly stuffy, should not be overly boring.

```html
<!DOCTYPE html>
<html lang="en">
<head>
<meta charset="utf-8">
<title>Mesa Ridge HR Consulting</title>
<link rel="stylesheet" href="https://fonts.googleapis.com/css2?family=Open+Sans:wght@300;400;600;700&family=Roboto+Condensed:wght@400;700&family=Exo+2:ital,wght@1,700;1,800&display=swap">
<style>
  :root {
    --red: #b31d2d;
    --red-dark: #8f1421;
    --red-light: #c82a3a;
    --black: #111111;
    --ink: #333333;
    --muted: #8a8a8a;
    --page: #ededed;
    --card: #f6f6f8;
    --white: #ffffff;
  }
  * { box-sizing: border-box; margin: 0; padding: 0; }
  html, body { width: 1200px; height: 1171px; overflow: hidden; }
  body { font-family: "Open Sans", Arial, sans-serif; background: var(--page); color: var(--ink); position: relative; }

  .site-header { position: absolute; left: 0; top: 0; width: 1200px; height: 140px; background: linear-gradient(#ffffff, #f1f1f1); }
  .brand { position: absolute; left: 150px; top: 40px; display: flex; align-items: center; gap: 12px; }
  .brand-mark { width: 26px; height: 26px; border-radius: 50%; background: var(--red); }
  .brand-name { font: 700 24px/1.1 "Open Sans", Arial, sans-serif; color: var(--black); width: 160px; }
  .call { position: absolute; right: 150px; top: 44px; display: flex; align-items: center; gap: 12px; }
  .call-icon { width: 46px; height: 46px; }
  .call-label { font-size: 16px; color: #555; line-height: 1.1; }
  .call-number { font: 700 24px/1.2 "Roboto Condensed", Arial, sans-serif; color: var(--black); letter-spacing: 0.5px; }

  .main-nav { position: absolute; left: 0; top: 140px; width: 1200px; height: 48px; background: linear-gradient(var(--red-light), var(--red) 55%, var(--red-dark)); }
  .main-nav ul { list-style: none; display: flex; margin-left: 150px; height: 48px; }
  .main-nav li { font: 400 19px/48px "Roboto Condensed", Arial, sans-serif; color: var(--white); padding: 0 29px; border-right: 1px solid rgba(0,0,0,0.18); }
  .main-nav li.is-active { background: linear-gradient(#2a2a2a, #000); }

  .hero { position: absolute; left: 0; top: 188px; width: 1200px; height: 440px; overflow: hidden; }
  .hero-photo { position: absolute; inset: 0; background: linear-gradient(#e9ecf0 0%, #cfd4da 45%, #aeb4bb 72%, #8d949b 100%); }
  .hero-faint-name { position: absolute; left: 100px; top: 60px; width: 270px; font: 700 40px/1.1 "Open Sans", Arial, sans-serif; color: rgba(120,120,120,0.25); }
  .video-play { position: absolute; left: 188px; top: 87px; width: 96px; height: 96px; }
  .hero-title { position: absolute; left: 438px; top: 68px; width: 640px; font: italic 800 40px/50px "Exo 2", Arial, sans-serif; color: var(--black); }
  .hero-more { position: absolute; left: 438px; top: 186px; font: italic 700 21px/1 "Exo 2", Arial, sans-serif; color: var(--black); }
  .hero-more span { color: var(--red); }
  .intro-tab { position: absolute; left: 150px; top: 291px; width: 234px; height: 33px; background: var(--black); color: var(--white); font: italic 700 18px/33px "Exo 2", Arial, sans-serif; padding-left: 18px; }
  .intro-box { position: absolute; left: 150px; top: 324px; width: 702px; height: 116px; background: var(--red); color: var(--white); font-size: 15px; line-height: 24.5px; padding: 18px 22px; }

  .services { position: absolute; left: 0; top: 628px; width: 1200px; height: 495px; background: var(--page); }
  .services-title { position: absolute; left: 0; width: 1200px; top: 45px; text-align: center; font-size: 20px; color: #222; letter-spacing: 0.5px; }
  .services-title::before, .services-title::after { content: ""; display: inline-block; width: 140px; height: 1px; background: #d2d2d2; vertical-align: middle; margin: 0 18px; }
  .services-sub { position: absolute; left: 0; width: 1200px; top: 80px; text-align: center; font: 300 16px/1 "Open Sans", Arial, sans-serif; color: var(--muted); }
  .service-card { position: absolute; top: 142px; width: 280px; height: 304px; background: var(--card); border: 1px solid #d4d4d4; }
  .service-card h3 { height: 48px; background: linear-gradient(#2b2b2b, #000); color: var(--white); font: italic 700 18px/48px "Exo 2", Arial, sans-serif; padding-left: 18px; }
  .service-card ul { list-style: none; padding: 16px 0 0 22px; }
  .service-card li { font-size: 12.5px; line-height: 27.2px; color: #555; padding-left: 21px; position: relative; }
  .service-card li::before { content: "\2727"; position: absolute; left: 0; font-size: 9px; color: #aaa; }
  .service-card a { position: absolute; left: 20px; bottom: 16px; font-size: 13px; font-style: italic; color: var(--red); text-decoration: none; }

  .site-footer { position: absolute; left: 0; top: 1123px; width: 1200px; height: 48px; background: var(--red); color: #f3d6d9; font-size: 12.5px; line-height: 48px; }
  .site-footer p { margin-left: 150px; }
  .social { position: absolute; right: 150px; top: 17px; display: flex; gap: 17px; }
  .social span { width: 14px; height: 14px; border-radius: 50%; background: var(--red-dark); }
  .social span.is-hover { background: #2a9fd8; }
</style>
</head>
<body>
  <header class="site-header">
    <div class="brand"><span class="brand-mark"></span><span class="brand-name">Mesa Ridge HR Consulting</span></div>
    <div class="call">
      <svg class="call-icon" viewBox="0 0 46 46" aria-hidden="true">
        <circle cx="23" cy="23" r="21" fill="none" stroke="#111" stroke-width="2.5"/>
        <path d="M16 14c1-1 2.5-1 3 0l2 3.5c.5 1 0 2-.8 2.6l-1.2 1c1 2.5 3 4.5 5.5 5.5l1-1.2c.6-.8 1.6-1.3 2.6-.8L31.6 27c1 .5 1 2 0 3l-1.6 1.6c-1.4 1.4-4 1.2-7-.8-3-2-5.6-4.6-7.6-7.6-2-3-2.2-5.6-.8-7z" fill="#111"/>
      </svg>
      <div>
        <div class="call-label">Questions? Call us at</div>
        <div class="call-number">(555) - 410 - 2876</div>
      </div>
    </div>
  </header>

  <nav class="main-nav">
    <ul>
      <li class="is-active">HOME</li>
      <li>ABOUT US</li>
      <li>SERVICES</li>
      <li>STAFFING</li>
      <li>PARTNERS</li>
      <li>OUR TEAM</li>
      <li>CONTACT US</li>
    </ul>
  </nav>

  <section class="hero">
    <div class="hero-photo" role="img" aria-label="Photo of a cloudy sky over a grey sea"></div>
    <div class="hero-faint-name">Mesa Ridge HR Consulting</div>
    <svg class="video-play" viewBox="0 0 96 96" aria-label="Play video" role="img">
      <circle cx="48" cy="48" r="42" fill="none" stroke="#000" stroke-width="9"/>
      <path d="M38 28 L68 48 L38 68 Z" fill="#000"/>
    </svg>
    <h1 class="hero-title">Lorem ipsum consectetur adipiscing Proin mattis leo sed</h1>
    <div class="hero-more">more information <span>›</span></div>
    <div class="intro-tab">Lorem ipsum dolor</div>
    <div class="intro-box">Lorem Ipsum is simply dummy text Lorem Ipsum has been the Tndustry's standard dummy text Ever since the 1500s, when an Unknown printer took a galley of Specimen book It has Only five centuries, but also the leap into electronic typesetting.</div>
  </section>

  <section class="services">
    <h2 class="services-title">MESA RIDGE SERVICES</h2>
    <p class="services-sub">Dolor sit amet, consectetur adipiscing Vestibulum ultrices tellus mi</p>

    <article class="service-card" style="left:148px">
      <h3>Lorem ipsum dolor</h3>
      <ul>
        <li>Lorem Ipsum is simply dummy text</li><li>Lorem Ipsum has been the</li><li>Tndustry's standard dummy text</li><li>Ever since the 1500s, when an</li><li>Unknown printer took a galley of</li><li>Specimen book. It has</li><li>Only five centuries, but also</li>
      </ul>
      <a href="#">View more →</a>
    </article>
    <article class="service-card" style="left:460px">
      <h3>Lorem ipsum dolor</h3>
      <ul>
        <li>Lorem Ipsum is simply dummy text</li><li>Lorem Ipsum has been the</li><li>Tndustry's standard dummy text</li><li>Ever since the 1500s, when an</li><li>Unknown printer took a galley of</li><li>Specimen book. It has</li><li>Only five centuries, but also</li>
      </ul>
      <a href="#">View more →</a>
    </article>
    <article class="service-card" style="left:770px">
      <h3>Lorem ipsum dolor</h3>
      <ul>
        <li>Lorem Ipsum is simply dummy text</li><li>Lorem Ipsum has been the</li><li>Tndustry's standard dummy text</li><li>Ever since the 1500s, when an</li><li>Unknown printer took a galley of</li><li>Specimen book. It has</li><li>Only five centuries, but also</li>
      </ul>
      <a href="#">View more →</a>
    </article>
  </section>

  <footer class="site-footer">
    <p>Copyright © 2014 Mesa Ridge Consulting. All Rights Reserved.</p>
    <div class="social" aria-label="Social links">
      <span></span><span class="is-hover"></span><span></span><span></span><span></span>
    </div>
  </footer>
</body>
</html>
```